Staffing Company Website

We need a website for a new company based out of central California called "Harvest Lane Staffing". We staff truck drivers for agriculture trucking businesses. We don't want a super corporate feel, we want something that feels more inviting to the kind of person who would work in Agriculture/Trucking while still being professional. Please let me know if you have any questions

```html
<!DOCTYPE html>
<html lang="en">
<head>
<meta charset="utf-8">
<title>Harvest Lane Staffing</title>
<link href="https://fonts.googleapis.com/css2?family=Poppins:wght@400;500;600;700;800&display=swap" rel="stylesheet">
<style>
:root{
  --red:#e30613;
  --dark:#111214;
  --ink:#1a1a1a;
  --grey:#6b6b6b;
  --light:#f1f1f1;
  --line:#e4e4e4;
  --white:#ffffff;
  --blue:#1d4fa3;
}
*{box-sizing:border-box;margin:0;padding:0}
html,body{width:1200px;height:5351px;overflow:hidden}
body{font-family:"Poppins",sans-serif;color:var(--ink);background:var(--white);position:relative}
.page{position:absolute;left:13px;top:67px;width:1174px}
.btn{display:inline-block;border-radius:30px;font-weight:700;font-size:11px;text-transform:uppercase;letter-spacing:.3px;padding:0 26px;height:34px;line-height:34px;text-align:center;white-space:nowrap}
.btn-red{background:var(--red);color:var(--white)}
.btn-outline{border:1.5px solid var(--red);color:var(--ink);background:var(--white)}
.section-title{font-size:36px;font-weight:800;text-align:center;letter-spacing:.5px;text-transform:uppercase}
.ph{display:block}

/* top bar + hero */
.topbar{height:22px;background:var(--red);color:var(--white);font-size:10px;display:flex;justify-content:space-between;align-items:center;padding:0 88px}
.topbar span{margin-left:24px}
.hero{position:relative;height:659px;overflow:hidden}
.hero-photo{position:absolute;inset:0;background:linear-gradient(180deg,#2f3236 0%,#3e4146 45%,#4b4f3c 75%,#5d8a2f 92%,#6fa23a 100%)}
.header{position:absolute;top:20px;left:0;right:0;padding:0 60px}
.header-main{display:flex;align-items:center;height:70px}
.brand{display:flex;align-items:center;gap:10px;color:var(--white);font-weight:700;font-size:15px;line-height:1.05;text-transform:uppercase;width:250px}
.brand-mark{width:40px;height:40px;border:3px solid var(--white)}
.search{width:240px;height:34px;border-radius:20px;background:#4a4d52;display:flex;align-items:center;justify-content:space-between;padding:0 4px 0 16px;color:#bfbfbf;font-size:11px;margin-left:2px}
.search i{width:26px;height:26px;border-radius:50%;background:var(--red);display:flex;align-items:center;justify-content:center}
.menu{display:flex;margin-left:auto;gap:22px;align-items:center;color:var(--white);font-size:11px;font-weight:600;text-transform:uppercase}
.flag{width:22px;height:15px;display:flex;flex-direction:column}
.flag b{flex:1}
.subnav{display:flex;align-items:center;gap:22px;color:#ddd;font-size:9.5px;text-transform:uppercase;font-weight:500;height:42px;border-top:1px solid rgba(255,255,255,.15)}
.subnav .btn{margin-left:auto;height:28px;line-height:28px;font-size:10px}
.hero-copy{position:absolute;left:95px;top:255px;color:var(--white)}
.hero-copy::before{content:"";position:absolute;left:-12px;top:-6px;width:8px;height:160px;background:var(--red)}
.hero-copy h1{font-size:50px;font-weight:800;line-height:1.18;text-transform:uppercase;letter-spacing:.5px}
.hero-copy h2{font-size:23px;font-weight:600;text-transform:uppercase;letter-spacing:1px;margin-top:2px}
.hero-copy p{font-size:13px;margin:26px 0 24px}

/* clients */
.brand-grid{width:800px;margin:0 auto;display:grid;grid-template-columns:repeat(5,1fr);grid-auto-rows:124px}
.brand-cell{display:flex;align-items:center;justify-content:center;text-align:center;border-right:1px solid var(--line);border-bottom:1px solid var(--line);font-weight:800;font-size:17px;line-height:1.2;color:#333;text-transform:uppercase;letter-spacing:.3px;padding:0 8px}
.brand-cell:nth-child(5n){border-right:none}
.brand-cell.active{background:var(--blue);color:var(--white);border-radius:6px;box-shadow:0 8px 18px rgba(0,0,0,.25)}

/* about */
.about{position:absolute;top:1308px;left:0;width:1174px;height:511px;display:flex;background:linear-gradient(90deg,#f7f7f7,#ececec)}
.about-photo{width:536px;height:100%;background:linear-gradient(180deg,#cfe3f1 0%,#b9d6e8 40%,#6b9a3a 62%,#4f7e2a 100%)}
.about-text{padding:107px 0 0 48px;width:440px}
.about-text h2{font-size:34px;font-weight:800;text-transform:uppercase}
.about-text h3{font-size:15px;font-weight:600;line-height:1.35;margin:6px 0 14px}
.about-text p{font-size:10.5px;line-height:1.6;color:#444;margin-bottom:20px}

/* cards */
.block{position:absolute;left:0;width:1174px;text-align:center}
.cards{width:800px;margin:0 auto;display:flex;gap:22px;text-align:left}
.card{flex:1;background:var(--white);border:1px solid var(--line);padding:14px;position:relative}
.card.lift{box-shadow:0 10px 28px rgba(0,0,0,.15);border-color:transparent}
.card-photo{height:200px;background:linear-gradient(180deg,#eceff2,#d4d8dc)}
.card h4{font-size:14px;font-weight:800;text-transform:uppercase;margin:18px 0 4px}
.card .price{color:var(--red);font-weight:700;font-size:14px}
.card.lift h4{color:var(--red)}
.specs{display:flex;gap:26px;margin:12px 0 18px;font-size:9.5px;color:#555}
.spec{display:flex;gap:6px;align-items:flex-start}
.spec b{display:block;font-weight:700;color:var(--ink);font-size:11px}
.card .btn{display:block;font-size:9.5px;padding:0 10px}
.view-all{margin-top:38px}
.date-tag{position:absolute;left:24px;top:24px;background:var(--white);color:var(--red);font-size:8.5px;font-weight:700;padding:3px 10px;border-radius:12px}
.card p{font-size:10.5px;line-height:1.55;color:#555;margin-bottom:16px;height:50px;overflow:hidden}
.card.news .btn{width:220px;margin:0 auto}

.agenda-cards{width:772px;margin:0 auto;display:flex;gap:38px;text-align:left}
.agenda-card{flex:1;border:1px solid var(--line);padding:12px;box-shadow:0 6px 18px rgba(0,0,0,.06);position:relative}
.agenda-card .card-photo{height:245px;background:linear-gradient(180deg,#b8c4d2 0%,#8a949e 55%,#6c6f74 100%)}
.agenda-card h4{font-size:18px;font-weight:800;text-transform:uppercase;margin:24px 0 6px}
.loc{display:flex;gap:6px;font-size:10.5px;color:#444;line-height:1.4;margin-bottom:22px}
.agenda-card .btn{display:block;font-size:9.5px}
.agenda-card .date-tag{background:var(--red);color:var(--white)}

/* driver match */
.config{position:absolute;top:3718px;left:0;width:1174px;height:511px;background:linear-gradient(90deg,#f2f2f2,#e9e9e9)}
.config-text{position:absolute;left:192px;top:85px;width:380px}
.config-text h2{font-size:34px;font-weight:800;text-transform:uppercase}
.config-text h3{font-size:15px;font-weight:600;line-height:1.3;margin:4px 0 14px}
.config-text p{font-size:10.5px;line-height:1.6;color:#444;margin-bottom:22px}
.config-photo{position:absolute;left:620px;top:58px;width:470px;height:400px;border-radius:10px;background:linear-gradient(160deg,#dfe3ea 0%,#5a6fa8 45%,#2c3b7c 70%,#d7d9dc 100%)}

/* what we haul */
.offer-grid{width:800px;margin:36px auto 0;display:grid;grid-template-columns:repeat(5,1fr);row-gap:34px}
.offer-item{display:flex;flex-direction:column;align-items:center;gap:12px;font-size:9px;font-weight:600;text-transform:uppercase;color:#333;line-height:1.25;text-align:center;padding:8px 4px}
.offer-item .ph{width:96px;height:72px;border-radius:6px;background:linear-gradient(180deg,#f0f0f0,#cfcfcf)}
.offer-item.active{box-shadow:0 8px 20px rgba(0,0,0,.15);color:var(--red)}

/* footer */
.footer{position:absolute;top:4856px;left:0;width:1174px;height:428px;background:var(--dark);color:var(--white)}
.footer-brand{position:absolute;left:88px;top:80px;display:flex;align-items:center;gap:26px}
.footer-brand .brand-mark{width:110px;height:110px;border-width:6px}
.footer-brand span{font-size:34px;font-weight:700;line-height:1.25;text-transform:uppercase;border-left:2px solid var(--white);padding-left:26px}
.fcol{position:absolute;top:60px;font-size:10px;line-height:2.2;color:#ccc}
.fcol h5{font-size:11px;font-weight:700;color:var(--white);text-transform:uppercase;margin-bottom:8px}
.fcol .hi{color:var(--white);font-weight:700;font-size:13px}
.fcol .red{color:var(--red)}
.footer-bottom{position:absolute;left:88px;right:88px;bottom:22px;display:flex;align-items:center;font-size:9.5px;color:#bbb;gap:24px;border-top:1px solid #2a2a2a;padding-top:16px}
.footer-bottom .socials{margin-left:auto;display:flex;gap:28px}
.footer-bottom .socials i{width:10px;height:10px;border-radius:50%;background:var(--white)}
</style>
</head>
<body>
<div class="page">
  <div class="topbar">
    <div>Follow us: <span>FB</span><span>IN</span></div>
    <div><span>info@harvestlane.example</span><span>(559) 555-0142</span></div>
  </div>

  <section class="hero">
    <div class="hero-photo ph" role="img" aria-label="Photo of a truck hauling a harvest load past Central Valley fields"></div>
    <header class="header">
      <div class="header-main">
        <div class="brand"><i class="brand-mark"></i>Harvest Lane<br>Staffing</div>
        <div class="search">Search jobs<i><svg width="12" height="12" viewBox="0 0 12 12"><circle cx="5" cy="5" r="3.5" fill="none" stroke="#fff" stroke-width="1.5"/><path d="M8 8l3 3" stroke="#fff" stroke-width="1.5"/></svg></i></div>
        <nav class="menu"><span>News</span><span>Employers</span><span>About us</span><span>Jobs</span><span>Contact</span><span>Apply</span>
          <span class="flag"><b style="background:#b22234"></b><b style="background:#fff"></b><b style="background:#3c3b6e"></b></span></nav>
      </div>
      <div class="subnav"><span>Harvest hauling</span><span>Livestock transport</span><span>Tanker &amp; bulk</span><span>Flatbed &amp; equipment</span><span>Seasonal routes</span><span>Yard &amp; shuttle</span><span class="btn btn-red">Apply now</span></div>
    </header>
    <div class="hero-copy">
      <h1>Truck drivers for<br>California farms</h1>
      <h2>Agricultural trucking staffing</h2>
      <p>Rooted in the Central Valley</p>
      <span class="btn btn-red">Watch video</span>
    </div>
  </section>

  <section class="block" style="top:748px">
    <h2 class="section-title" style="margin:40px 0 32px">Farms we drive for</h2>
    <div class="brand-grid">
      <div class="brand-cell">Valley Haul</div><div class="brand-cell">Sierra Grain</div><div class="brand-cell">Kings Dairy</div><div class="brand-cell">Tule Farms</div><div class="brand-cell">Westfork</div>
      <div class="brand-cell">Madera Hay</div><div class="brand-cell">Oak Creek</div><div class="brand-cell active">Fresno Ag</div><div class="brand-cell">Delta Nut</div><div class="brand-cell">Redline</div>
      <div class="brand-cell">Mesa Feed</div><div class="brand-cell">Pine Row</div><div class="brand-cell">Tolliver</div><div class="brand-cell">Marrow</div>
    </div>
  </section>

  <section class="about">
    <div class="about-photo ph" role="img" aria-label="Photo of a driver beside a farm truck in an orchard"></div>
    <div class="about-text">
      <h2>About us</h2>
      <h3>Good drivers and good farms, matched with care right here in the Central Valley</h3>
      <p>Harvest Lane Staffing connects experienced truck drivers with agricultural trucking businesses across Central California. We know the work: early starts at the packing shed, long runs during harvest, dairy pickups that can't wait and hay loads that have to be strapped right. Our team grew up around farms and fleets, so we listen first and match drivers to routes, schedules and equipment that fit. Drivers get steady work, fair pay and a real person to call. Employers get licensed, safety-minded drivers who show up ready for the season.</p>
      <span class="btn btn-red">Learn more</span>
    </div>
  </section>

  <section class="block" style="top:1900px">
    <h2 class="section-title" style="margin-bottom:24px">Open driver jobs</h2>
    <div class="cards">
      <article class="card">
        <div class="card-photo ph" role="img" aria-label="Photo of a truck loaded with harvest bins"></div>
        <h4>CDL-A Harvest Hauler</h4><div class="price">$32.50 / hour</div>
        <div class="specs"><div class="spec"><svg width="12" height="12"><rect x="1" y="2" width="10" height="9" fill="none" stroke="#888"/></svg><div>Season<b>2024</b></div></div><div class="spec"><svg width="12" height="12"><circle cx="6" cy="6" r="5" fill="none" stroke="#888"/></svg><div>Location<b>Fresno</b></div></div></div>
        <span class="btn btn-outline">Interested? Apply now</span>
      </article>
      <article class="card lift">
        <div class="card-photo ph" role="img" aria-label="Photo of a livestock trailer at a ranch"></div>
        <h4>Livestock Driver</h4><div class="price">Pay on request</div>
        <div class="specs"><div class="spec"><svg width="12" height="12"><rect x="1" y="2" width="10" height="9" fill="none" stroke="#888"/></svg><div>Season<b>2024</b></div></div><div class="spec"><svg width="12" height="12"><rect x="1" y="1" width="10" height="10" fill="none" stroke="#888"/></svg><div>Job number<b>#69524</b></div></div></div>
        <span class="btn btn-red">Interested? Apply now</span>
      </article>
      <article class="card">
        <div class="card-photo ph" role="img" aria-label="Photo of a milk tanker truck at a dairy"></div>
        <h4>Tanker Driver</h4><div class="price">$34.00 / hour</div>
        <div class="specs"><div class="spec"><svg width="12" height="12"><rect x="1" y="2" width="10" height="9" fill="none" stroke="#888"/></svg><div>Season<b>2024</b></div></div><div class="spec"><svg width="12" height="12"><rect x="1" y="1" width="10" height="10" fill="none" stroke="#888"/></svg><div>Job number<b>#69756</b></div></div></div>
        <span class="btn btn-outline">Interested? Apply now</span>
      </article>
    </div>
    <span class="btn btn-red view-all">View all</span>
  </section>

  <section class="block" style="top:2520px">
    <h2 class="section-title" style="margin-bottom:24px">Latest news</h2>
    <div class="cards">
      <article class="card news">
        <div class="card-photo ph" role="img" aria-label="Photo of trucks lined up at a packing shed"></div><span class="date-tag">● 28 JUL 2024</span>
        <h4>Harvest hiring open</h4><p>Tomato and almond season is close. We are booking CDL-A drivers now for steady runs from field to processor.</p>
        <span class="btn btn-outline">Read more</span>
      </article>
      <article class="card news lift">
        <div class="card-photo ph" role="img" aria-label="Photo of a new truck yard"></div><span class="date-tag">● 28 JUL 2024</span>
        <h4>New Fresno office</h4><p>Our new office sits right off Highway 99, so drivers can stop by, meet the team and pick up paperwork fast.</p>
        <span class="btn btn-red">Read more</span>
      </article>
      <article class="card news">
        <div class="card-photo ph" role="img" aria-label="Photo of drivers at a safety training"></div><span class="date-tag">● 28 JUL 2024</span>
        <h4>Safety week recap</h4><p>Load securement, heat safety and backing drills. Thanks to every driver who joined us in the yard this week.</p>
        <span class="btn btn-outline">Read more</span>
      </article>
    </div>
    <span class="btn btn-red view-all">View all</span>
  </section>

  <section class="block" style="top:3120px">
    <h2 class="section-title" style="margin-bottom:24px">Hiring events</h2>
    <div class="agenda-cards">
      <article class="agenda-card">
        <div class="card-photo ph" role="img" aria-label="Photo of trucks parked in a row at a hiring day"></div><span class="date-tag">10 AUG 2024 · 9 AM – 2 PM</span>
        <h4>Fresno driver day</h4>
        <div class="loc"><svg width="12" height="14" viewBox="0 0 12 14"><path d="M6 13S1 8 1 5a5 5 0 0 1 10 0c0 3-5 8-5 8z" fill="none" stroke="#e30613" stroke-width="1.5"/><circle cx="6" cy="5" r="1.6" fill="#e30613"/></svg><span>1240 Orchard Ave,<br>Fresno, CA 93721</span></div>
        <span class="btn btn-red">View details</span>
      </article>
      <article class="agenda-card">
        <div class="card-photo ph" role="img" aria-label="Photo of a job fair at a county fairground"></div><span class="date-tag">24 AUG 2024 · 10 AM – 3 PM</span>
        <h4>Modesto job fair</h4>
        <div class="loc"><svg width="12" height="14" viewBox="0 0 12 14"><path d="M6 13S1 8 1 5a5 5 0 0 1 10 0c0 3-5 8-5 8z" fill="none" stroke="#e30613" stroke-width="1.5"/><circle cx="6" cy="5" r="1.6" fill="#e30613"/></svg><span>Fairground Hall B,<br>Modesto, CA 95354</span></div>
        <span class="btn btn-red">View details</span>
      </article>
    </div>
  </section>

  <section class="config">
    <div class="config-text">
      <h2>Driver match</h2>
      <h3>Tell us how you like to drive and we will find the farm route that fits you</h3>
      <p>Pick your license class, the loads you know, your home base and the hours that work for you. Day runs, overnight hauls, seasonal harvest work or year-round dairy routes: our recruiters check every answer and call you back within one business day. No long forms, no pressure, just honest options. Employers can use the same tool to tell us what they need, from a single relief driver to a full crew for the busy months. Once we find a fit, we handle the paperwork so you can get rolling.</p>
      <span class="btn btn-red">Get matched</span>
    </div>
    <div class="config-photo ph" role="img" aria-label="Photo of a blue farm truck parked beside an orchard"></div>
  </section>

  <section class="block" style="top:4308px">
    <h2 class="section-title">What we haul</h2>
    <div class="offer-grid">
      <div class="offer-item"><i class="ph" role="img" aria-label="Photo of row crop loads"></i>Row crops</div>
      <div class="offer-item"><i class="ph" role="img" aria-label="Photo of a livestock trailer"></i>Livestock<br>transport</div>
      <div class="offer-item"><i class="ph" role="img" aria-label="Photo of a milk tanker"></i>Dairy &amp;<br>milk tankers</div>
      <div class="offer-item"><i class="ph" role="img" aria-label="Photo of a grain truck"></i>Grain &amp;<br>feed</div>
      <div class="offer-item"><i class="ph" role="img" aria-label="Photo of tomato gondolas"></i>Tomatoes &amp;<br>produce</div>
      <div class="offer-item"><i class="ph" role="img" aria-label="Photo of nut trailers"></i>Almonds</div>
      <div class="offer-item"><i class="ph" role="img" aria-label="Photo of hay bales on a flatbed"></i>Hay &amp;<br>straw</div>
      <div class="offer-item active"><i class="ph" role="img" aria-label="Photo of a flatbed trailer"></i>Flatbed &amp;<br>trailers</div>
      <div class="offer-item"><i class="ph" role="img" aria-label="Photo of a refrigerated trailer"></i>Reefer loads</div>
      <div class="offer-item"><i class="ph" role="img" aria-label="Photo of a lowboy with farm equipment"></i>Equipment moves</div>
    </div>
    <span class="btn btn-red view-all" style="margin-top:22px">View all</span>
  </section>

  <footer class="footer">
    <div class="footer-brand"><i class="brand-mark"></i><span>Harvest Lane<br>Staffing</span></div>
    <div class="fcol" style="left:490px"><h5>Navigation</h5>News<br>Employers<br>About us<br>Jobs<br>Contact<br>Apply</div>
    <div class="fcol" style="left:641px"><h5>Driver jobs</h5>Harvest hauling<br>Livestock transport<br>Tanker &amp; bulk<br>Flatbed &amp; equipment<br>Seasonal routes<br>Yard &amp; shuttle<br>All openings</div>
    <div class="fcol" style="left:842px"><h5>Address</h5>1240 Orchard Ave<br>Fresno, CA 93721<br><span class="hi">(559) 555-0142</span><br><span class="red">info@harvestlane.example</span></div>
    <div class="footer-bottom"><span>©2024 Harvest Lane Staffing. All Rights Reserved.</span><span>Privacy Policy</span><span>Terms &amp; Conditions</span><span class="socials"><i></i><i></i><i></i><i></i></span></div>
  </footer>
</div>
</body>
</html>
```